A new fresh and flat K&T Logistics Brochure Design A4 - 4 pages

Our client is an established International Logistics firm looking to upgrade their sales brochure.
We would like the designer to create concepts that are flat, modern and communicate reliability and expediency to our clients. We want the brochure to maintain a degree of white space and minimal design.
Introduction
LOGISTICS - it's what we do best! We're proud to say so after 27 years (and counting) of organic growth within the 3PL industry. Starting off in Meridian, Mississippi with a fleet of 4 trucks in 1987, K&T is today a global 3PL company with offices in the United States and Asia Pacific region.
Our goal has always been to serve our clients by getting things done, and getting them done right.
Format: A4 4-sided brochure
Pg 1 Front Page - Company name and logo, and vector design concept to make front page unique. Please try to include some kind of container reference design on the front page (e.g 2D or 3D vector, transparent overlay etc...), place this design element somewhere in the middle or bttom of the page.
Pg 2 and/or Pg 3
- Introduction and Core services Including: ABOUT, SERVICES, CONTRACT LOGISTICS, K&T INTEL (following the menu content of our website www.ktwrx.example)
- Text space to explain Services in more detail.
Social proof (existing client testimonials/feedback.)
- A 'C.A.R.E' acronym design element, including the words: Communicative, Accessible, Responsible, Efficient
Pg 4 Back Page- Contact information, Call to action.
Throughut the brochure please leave space for images as you deem appropriate and we will update late OR even better usesome of your own stock images.
Color theme: Based on corporate colors (but not limited to), see website
http://www.ktwrx.example
Try diffent font types to the website both serif and sans serif
Include several CTAs throughout the brochure.
You can use both the attached pdf brochure and the website for content.
We would also appreciate if you could also enhance the logo to make it 'pop' (keep shape and style).

```html
<!DOCTYPE html>
<html lang="en">
<head>
<meta charset="utf-8">
<title>K&amp;T Logistics – Services Spread</title>
<link href="https://fonts.googleapis.com/css2?family=Open+Sans:wght@300;400;700&family=Oswald:wght@400;700&display=swap" rel="stylesheet">
<style>
:root{
  --orange:#f39322;
  --slate:#45657e;
  --slate-dark:#3a566c;
  --ink:#2c2c2c;
  --paper:#ffffff;
  --backdrop:#ffffff;
}
*{box-sizing:border-box;margin:0;padding:0}
html,body{width:1200px;height:1000px;overflow:hidden;background:var(--backdrop)}
body{position:relative;font-family:"Open Sans",Arial,sans-serif;color:var(--ink)}
.spread{position:absolute;left:35px;top:100px;width:1130px;height:810px;background:var(--paper);box-shadow:0 0 14px rgba(0,0,0,.25)}
.section-number{position:absolute;font-family:"Oswald",Arial,sans-serif;font-weight:700;color:var(--slate);font-size:74px;line-height:1;transform:scaleX(.92);transform-origin:left top}
.section-title{position:absolute;height:36px;background:var(--orange);color:#fff;font-weight:300;font-size:21px;line-height:36px;padding-left:9px;letter-spacing:-.2px;white-space:nowrap;clip-path:polygon(0 0,100% 0,calc(100% - 20px) 100%,0 100%)}
.rail{position:absolute;width:4px;background:var(--orange)}
.sub-head{position:absolute;height:22px}
.sub-head .tab{position:absolute;left:0;top:0;height:22px;width:152px;background:var(--slate);color:#fff;font-weight:700;font-size:13px;line-height:22px;padding-left:10px;clip-path:polygon(0 0,100% 0,calc(100% - 14px) 100%,0 100%)}
.sub-head .line{position:absolute;left:0;top:0;height:4px;background:var(--slate)}
.body-copy{position:absolute;font-size:8px;line-height:11.4px;color:var(--ink)}
.body-copy p+p{margin-top:9px}
.photo{position:absolute}
.photo-sea{background:linear-gradient(160deg,#dbe8f2,#8eaac3 55%,#46657f)}
.photo-air{background:linear-gradient(150deg,#7f9bb4,#c9d8e5 60%,#e9f0f6)}
.photo-land{background:linear-gradient(180deg,#45657e 0 22px,#b9cddd 22px,#eef3f7 70%,#9db3c6)}
.photo-hub{background:linear-gradient(180deg,#45657e 0 22px,#a9bfd1 22px,#e4ecf2 60%,#7893ab)}
.photo-cfs{background:linear-gradient(170deg,#c5d5e2,#7b97b0 60%,#4b6a83)}
.photo-city{background:radial-gradient(ellipse at 60% 70%,#d8f0ff 0,#5fb6e0 25%,#1c4f7c 60%,#0a2240 100%)}
.intel-mark{position:absolute;left:836px;top:435px;width:290px;height:126px;background:linear-gradient(180deg,#f5f7f9,#e3e9ee);border:1px solid #d9dee3;border-radius:6px;display:flex;align-items:center;justify-content:center}
.intel-mark span{font-weight:700;font-size:38px;color:var(--slate)}
.service-list{position:absolute;left:643px;top:522px;list-style:none}
.service-list li{display:flex;align-items:center;height:33.6px;font-size:8px}
.service-list svg{width:24px;height:24px;margin-right:13px;flex:none}
.contact-bar{position:absolute;left:50px;top:860px;width:1107px;height:56px;background:var(--orange);border:4px solid var(--slate-dark);border-bottom:none;border-radius:14px 14px 0 0;display:flex;align-items:center;padding-left:24px;color:#fff;font-family:"Oswald",Arial,sans-serif;font-size:19px;letter-spacing:.1px;white-space:nowrap}
.contact-bar svg{flex:none}
.contact-bar .sep{margin:0 8px}
.contact-bar .dot{width:11px;height:11px;border-radius:50%;background:var(--slate-dark);margin:0 18px;flex:none}
</style>
</head>
<body>
<main class="spread">

  <div class="section-number" style="left:20px;top:15px">1</div>
  <h2 class="section-title" style="left:55px;top:22px;width:272px">Freight &amp; Transportation</h2>
  <div class="rail" style="left:55px;top:56px;height:704px"></div>

  <div class="sub-head" style="left:62px;top:72px;width:336px"><div class="line" style="width:336px"></div><div class="tab">Sea Freight</div></div>
  <div class="body-copy" style="left:72px;top:105px;width:320px">Equipped to handle Port-to-Port or Multimodal shipments to all regions across the globe, K&amp;T is your one stop shop for any and all of your sea freight needs! As a licensed NVOCC, we take pride in the responsibility you place in our hands to handle your shipments with the utmost of diligence and efficiency. Whether you're in need of shipping Containerized, LCL, or Project cargo, look no further than K&amp;T to do justice to your shipping requirements.</div>
  <div class="photo photo-sea" role="img" aria-label="Container port with cranes at dusk" style="left:400px;top:70px;width:151px;height:102px"></div>

  <div class="sub-head" style="left:62px;top:185px;width:336px"><div class="line" style="width:336px"></div><div class="tab">Air Freight</div></div>
  <div class="body-copy" style="left:72px;top:220px;width:320px">With strong tie ups to major air carriers, and a trusted network of partners at most global airports, we're confident in our ability to deliver on your time sensitive shipments.</div>
  <div class="photo photo-air" role="img" aria-label="Cargo aircraft being loaded on the apron" style="left:400px;top:185px;width:151px;height:101px"></div>

  <div class="sub-head" style="left:62px;top:298px;width:336px"><div class="line" style="width:336px"></div><div class="tab">Land Transport</div></div>
  <div class="body-copy" style="left:72px;top:332px;width:320px">With over 25 years of experience in the trucking business and a fleet thats grown organically from 4 trucks in 1987, to over 30 trucks in 2013, we're proud of the inroads we have made in the trucking sector. We're equipped to truck anywhere in the 48 contiguous states of the USA and if you need trucking outside the US - we've got long-standing partners in most of continental Europe as well as infrastructure in China that helps ensure we're present globally to cover your land transportation requirements.</div>
  <div class="photo photo-land" role="img" aria-label="White freight truck on an open road" style="left:400px;top:298px;width:151px;height:101px"></div>

  <div class="section-number" style="left:16px;top:433px">2</div>
  <h2 class="section-title" style="left:55px;top:438px;width:338px">Warehousing &amp; Distribution</h2>

  <div class="sub-head" style="left:62px;top:490px;width:336px"><div class="line" style="width:336px"></div><div class="tab">Distribution Hubs</div></div>
  <div class="body-copy" style="left:72px;top:522px;width:320px"><p>Fully racked and equipped with a multi-purpose warehouse management system - we're positive our sites have the tools to make your distribution cycle run like clockwork!</p><p>We offer a full suite of on-site logistics such as kitting, bundling, re- packing and pick/pack, and if you're needing to store temperature sensitive cargo, our cold storage locations allow you to make sure your product is sitting in the climate you intended for it!</p></div>
  <div class="photo photo-hub" role="img" aria-label="Large racked warehouse interior" style="left:400px;top:490px;width:151px;height:101px"></div>

  <div class="sub-head" style="left:62px;top:618px;width:336px"><div class="line" style="width:336px"></div><div class="tab">CFS Consolidations</div></div>
  <div class="body-copy" style="left:72px;top:650px;width:320px"><p>Several importers utilize CFS (container freight station) facilities to bundle the products they've bought across multiple suppliers into consolidated containers.</p><p style="margin-top:4px">The CFS option serves as a cost effective alternative to shipping LCL (less-than-container) loads by saving on freight and economizing on transit time.</p><p style="margin-top:4px">K&amp;T has dedicated CFS stations at most major Asian origins (China, Taiwan, Vietnam, Indonesia &amp; Thailand) so as to ensure that your products are bundled and routed on to your desired destination safely and timely.</p></div>
  <div class="photo photo-cfs" role="img" aria-label="Stacked shipping containers in a freight yard" style="left:400px;top:618px;width:151px;height:101px"></div>

  <div class="section-number" style="left:584px;top:15px">3</div>
  <h2 class="section-title" style="left:625px;top:22px;width:272px">Fulfillment &amp; Retail</h2>
  <div class="rail" style="left:625px;top:56px;height:704px"></div>
  <div class="body-copy" style="left:640px;top:68px;width:180px"><p>Our fully integrated order processing and fulfillment system allows us to act as your virtual office, so that you don't need one!</p><p>Ideal for online sellers or businesses that need a presence in foreign regions, the fulfillment system serves as a web based B2B or B2C communication tool that's easy and convenient to use while still granting you the ability to establish the checks and balances you need that ensure robustness and security to your operations.</p><p>The system is also set up to provide you with reports related to your sales orders and invoices on the back-end, while simultaneously allowing your clients to order what's in stock or soon available for dispatch on the front end, thereby allowing for the seamless intergration of your supply chain right from procurement thru delivery!</p></div>
  <div class="photo photo-city" role="img" aria-label="City skyline at night with light trails of traffic" style="left:837px;top:70px;width:287px;height:189px"></div>

  <div class="section-number" style="left:580px;top:380px">4</div>
  <h2 class="section-title" style="left:625px;top:386px;width:272px">K&amp;T Intel</h2>
  <div class="body-copy" style="left:640px;top:432px;width:184px"><p>Covering complex supply chains, multiple networks and varying life cycles, K&amp;T Intel is our flagship software service that allows you to stay on top of your operation.</p><p>Our range of software services thru K&amp;T Intel extends to:</p></div>
  <div class="intel-mark"><span>K&amp;T Intel</span></div>

  <ul class="service-list">
    <li><svg viewBox="0 0 24 24" fill="none" stroke="#222" stroke-width="1.4"><path d="M2 4h3l3 11h11l2-8H7"/><circle cx="9" cy="19" r="1.6"/><circle cx="18" cy="19" r="1.6"/></svg>Vendor Management</li>
    <li><svg viewBox="0 0 24 24" fill="none" stroke="#222" stroke-width="1.4"><path d="M2 6h3l3 9h11l2-7"/><rect x="9" y="5" width="8" height="6"/><circle cx="9" cy="19" r="1.6"/><circle cx="18" cy="19" r="1.6"/></svg>Order Management</li>
    <li><svg viewBox="0 0 24 24" fill="none" stroke="#222" stroke-width="1.4"><rect x="5" y="3" width="14" height="19"/><rect x="9" y="1.5" width="6" height="3" fill="#222"/><rect x="7.5" y="8" width="3" height="3"/><rect x="7.5" y="14" width="3" height="3"/><path d="M12 9.5h5M12 15.5h5"/></svg>Inventory Management and Visibility</li>
    <li><svg viewBox="0 0 24 24"><path d="M2 11L12 3l10 8v11H2z" fill="#222"/><rect x="7" y="14" width="10" height="8" fill="#fff"/><path d="M7 16h10M7 18h10M7 20h10" stroke="#222" stroke-width="1"/></svg>Warehouse Management</li>
    <li><svg viewBox="0 0 24 24" fill="none" stroke="#222" stroke-width="1.4"><rect x="2" y="8" width="13" height="9"/><path d="M15 11h4l3 3v3h-7"/><circle cx="6" cy="19" r="1.8"/><circle cx="18" cy="19" r="1.8"/><circle cx="8.5" cy="4.5" r="2.5"/></svg>In-Transit Cargo Track and Trace at SKU Levels</li>
    <li><svg viewBox="0 0 24 24" fill="none" stroke="#222" stroke-width="1.4"><rect x="2" y="3" width="20" height="18"/><rect x="5" y="12" width="3" height="7" fill="#222"/><rect x="10" y="8" width="3" height="11" fill="#222"/><rect x="15" y="10" width="3" height="9" fill="#222"/></svg>Financial and Operational Performance Reporting</li>
  </ul>
</main>

<footer class="contact-bar">
  <svg width="22" height="24" viewBox="0 0 22 24"><rect x="1" y="2" width="6" height="20" rx="2" fill="#fff"/><rect x="9" y="4" width="12" height="18" rx="2" fill="#fff"/><g fill="#f39322"><rect x="11" y="6" width="8" height="4"/><rect x="11" y="12" width="2" height="2"/><rect x="14" y="12" width="2" height="2"/><rect x="17" y="12" width="2" height="2"/><rect x="11" y="16" width="2" height="2"/><rect x="14" y="16" width="2" height="2"/><rect x="17" y="16" width="2" height="2"/></g></svg>
  <span style="margin-left:8px">+1 (555) 010 4821 (US)</span><span class="sep">|</span><span>+86 (755) 0100 2234 (Asia)</span><span class="sep" style="margin-left:12px">|</span><span>+852 0100 5678 (HK)</span>
  <span class="dot"></span>
  <svg width="26" height="22" viewBox="0 0 26 22"><path d="M1 8l12-7 12 7v13H1z" fill="#fff"/><path d="M1 8l12 8 12-8" fill="none" stroke="#f39322" stroke-width="1.6"/></svg>
  <span style="margin-left:10px">info@ktfreight.example</span>
  <span class="dot"></span>
  <svg width="24" height="24" viewBox="0 0 24 24"><circle cx="12" cy="12" r="11" fill="#fff"/><path d="M6 6c3 1 4 4 2 6s1 5 3 5M15 3c-1 3 2 4 4 4M18 13c-2 1-2 4 0 6" fill="none" stroke="#f39322" stroke-width="2"/></svg>
  <span style="margin-left:12px">www.ktwrx.example</span>
</footer>
</body>
</html>
```